Online Jewellery Marketing Design Project

I need a simple colour business card with a style that can easily be transferred into grayscale and can be used for as part of the design for brochures and gift certificates.

Design to revolve around Script, Peacock feathers and the colours found in them. I would also be open to a rich purple.

The business is a small discount online jewellery and painting sales. As business improves the designs will need to be able to be used on the card backings of the jewellery, a website with cart capability and other marketing tools.

The final design should communicate inexpensive style.

I have include some of the designs I have been using while this was just a hobby. Now that it is moving towards a proper business, even if only part time, a more professional touch is required.

Industry/Entity Type

Marketing

Logo Text

Mel's Marigold Jewellery & Paintings

```html
<!DOCTYPE html>
<html lang="en">
<head>
<meta charset="utf-8">
<title>Mel's Marigold – Business Card</title>
<link rel="stylesheet" href="https://fonts.googleapis.com/css2?family=Dancing+Script:wght@500;700&display=swap">
<style>
  :root {
    --backdrop: #2a2a2a;
    --card-black: #0c0c0c;
    --ink-white: #f2f2f2;
    --ink-grey: #cfcfcf;
    --feather-deep: #1d2a1c;
    --feather-green: #3c5a2e;
    --feather-teal: #2b6f6c;
    --feather-blue: #23357a;
    --swatch-orange: #d8662a;
    --swatch-blue: #3b5fa8;
  }
  * { margin: 0; padding: 0; box-sizing: border-box; }
  html, body {
    width: 1200px; height: 900px; overflow: hidden;
    background: var(--backdrop);
  }
  .card {
    position: absolute; left: 180px; top: 210px;
    width: 840px; height: 480px;
    background: var(--card-black);
    box-shadow: 0 10px 30px rgba(0,0,0,.6);
    overflow: hidden;
    font-family: "Dancing Script", cursive;
  }
  .card-art { position: absolute; inset: 0; }
  .brand {
    position: absolute; left: 70px; top: 90px;
    color: var(--ink-white); font-weight: 700; line-height: 1;
  }
  .brand-name { font-size: 54px; }
  .brand-tagline { font-size: 30px; margin: 6px 0 0 30px; }
  .contact {
    position: absolute; left: 40px; top: 245px; width: 460px;
    text-align: center; color: var(--ink-grey);
    font-size: 27px; font-weight: 500; line-height: 1.45;
  }
  .links {
    position: absolute; left: 80px; top: 360px;
    list-style: none; color: var(--ink-grey);
    font-size: 22px; font-weight: 500; line-height: 1.55;
  }
  .links li { display: flex; align-items: center; gap: 12px; }
  .links .marker { width: 14px; height: 10px; flex: none; }
  .marker--shop { background: var(--swatch-orange); }
  .marker--social { background: var(--swatch-blue); border-radius: 50%; width: 10px; }
</style>
</head>
<body>
  <div class="card">
    <svg class="card-art" viewBox="0 0 840 480" width="840" height="480">
      <defs>
        <linearGradient id="featherTones" x1="0" y1="0" x2="1" y2="1">
          <stop offset="0" stop-color="var(--feather-green)"/>
          <stop offset="0.35" stop-color="var(--feather-teal)"/>
          <stop offset="0.6" stop-color="var(--feather-blue)"/>
          <stop offset="1" stop-color="var(--feather-deep)"/>
        </linearGradient>
      </defs>
      <path class="feather-panel" role="img" aria-label="Close-up photograph of peacock tail feathers"
            d="M480 0 C420 70 440 150 520 230 C590 300 620 390 560 480 L840 480 L840 0 Z"
            fill="url(#featherTones)"/>
      <path class="panel-edge" d="M480 0 C420 70 440 150 520 230 C590 300 620 390 560 480"
            fill="none" stroke="var(--ink-white)" stroke-width="4"/>
      <path class="panel-edge-swell" d="M590 340 C600 400 590 440 540 480 L560 480 C610 430 612 390 590 340 Z"
            fill="var(--ink-white)"/>
    </svg>

    <div class="brand">
      <div class="brand-name">Mel's Marigold</div>
      <div class="brand-tagline">Jewellery &amp; Paintings</div>
    </div>

    <div class="contact">
      <p>MelsMarigold@mailbox.com</p>
      <p>stall.shopmart.com.au/melsmarigold/</p>
    </div>

    <ul class="links">
      <li><span class="marker marker--shop"></span>www.Craftly.com/shop/MelsMarigold</li>
      <li><span class="marker marker--social"></span>www.Friendbook.com/MelsMarigold</li>
    </ul>
  </div>
</body>
</html>
```